Body therapist needs a business card

I need a card for my business which is teaching trainings in body therapy, the company is called Wexcombe Educational Group. I teach to massage therapists around Australia, South East Asia and the USA. I am attaching my logo which will guide you as to what colours I would like to have you consider. Please consult my website to find out more about what I do. www.corvantela.com.au

My name is Daniel Wexcombe. My phone number is (03) 9417 2608 or 0461753208. email is info@corvantela.com.au

```html
<!DOCTYPE html>
<html lang="en">
<head>
<meta charset="utf-8">
<title>Wexcombe Educational Group – Business Card</title>
<link href="https://fonts.googleapis.com/css2?family=Poppins:wght@400;500;700&display=swap" rel="stylesheet">
<style>
  :root {
    --bg: #6f6f6f;
    --card: #ffffff;
    --brown: #8e5225;
    --brown-dark: #5a2a1a;
    --red: #b01f24;
    --lime: #cddc2e;
  }
  * { box-sizing: border-box; margin: 0; padding: 0; }
  html, body { width: 1200px; height: 1200px; overflow: hidden; }
  body {
    background: var(--bg);
    font-family: "Poppins", sans-serif;
    position: relative;
  }
  .card {
    position: absolute;
    left: 220px;
    width: 760px;
    height: 434px;
    background: var(--card);
    border-radius: 26px;
    box-shadow: 0 6px 18px rgba(0,0,0,0.25);
  }
  .card--front { top: 130px; }
  .card--back { top: 636px; }

  /* Front */
  .front-brand {
    position: absolute;
    inset: 0;
    display: flex;
    flex-direction: column;
    align-items: center;
    justify-content: center;
  }
  .brand-dot {
    width: 92px;
    height: 92px;
    border-radius: 50%;
    background: var(--brown);
    margin-bottom: 26px;
  }
  .brand-name {
    font-size: 62px;
    font-weight: 400;
    color: var(--brown-dark);
    line-height: 1;
    letter-spacing: 0.5px;
  }
  .brand-sub {
    margin-top: 8px;
    font-size: 25px;
    font-weight: 400;
    color: var(--red);
    letter-spacing: 0.5px;
  }

  /* Back */
  .back-brand {
    position: absolute;
    left: 70px;
    top: 0;
    bottom: 0;
    width: 250px;
    display: flex;
    align-items: center;
    gap: 14px;
  }
  .back-brand .brand-dot {
    width: 40px;
    height: 40px;
    margin: 0;
    flex: none;
  }
  .back-brand .brand-word {
    font-size: 34px;
    font-weight: 400;
    color: var(--brown-dark);
  }
  .divider {
    position: absolute;
    left: 350px;
    top: 108px;
    width: 2px;
    height: 218px;
    background: var(--lime);
  }
  .contact {
    position: absolute;
    left: 385px;
    top: 112px;
    color: var(--red);
  }
  .contact-name {
    font-size: 24px;
    font-weight: 700;
    text-transform: uppercase;
    line-height: 1.1;
  }
  .contact-role {
    font-size: 16px;
    color: var(--brown);
    margin-bottom: 14px;
  }
  .contact-list { list-style: none; }
  .contact-item {
    display: flex;
    align-items: flex-start;
    gap: 10px;
    font-size: 17px;
    color: var(--brown);
    line-height: 1.35;
    margin-bottom: 6px;
  }
  .contact-item svg {
    width: 16px;
    height: 16px;
    flex: none;
    margin-top: 4px;
    fill: var(--red);
  }
</style>
</head>
<body>

  <section class="card card--front">
    <div class="front-brand">
      <span class="brand-dot"></span>
      <div class="brand-name">Wexcombe</div>
      <div class="brand-sub">Educational Group</div>
    </div>
  </section>

  <section class="card card--back">
    <div class="back-brand">
      <span class="brand-dot"></span>
      <span class="brand-word">Wexcombe</span>
    </div>

    <div class="divider"></div>

    <div class="contact">
      <div class="contact-name">Daniel Wexcombe</div>
      <div class="contact-role">Manager</div>
      <ul class="contact-list">
        <li class="contact-item">
          <svg viewBox="0 0 16 16" aria-hidden="true"><path d="M8 0a5.5 5.5 0 0 0-5.5 5.5C2.5 10 8 16 8 16s5.5-6 5.5-10.5A5.5 5.5 0 0 0 8 0zm0 8a2.5 2.5 0 1 1 0-5 2.5 2.5 0 0 1 0 5z"/></svg>
          <span>Harlow Park Victoria,<br>3190 Australia</span>
        </li>
        <li class="contact-item">
          <svg viewBox="0 0 16 16" aria-hidden="true"><path d="M3.6 1.2 5.8 3.4c.4.4.4 1 0 1.4L4.6 6a9 9 0 0 0 5.4 5.4l1.2-1.2c.4-.4 1-.4 1.4 0l2.2 2.2c.4.4.4 1 0 1.4l-1.3 1.3C11.8 16 4 11 0.9 3.7 0.6 3 .9 2.3 1.3 1.9L2.2 1.2c.4-.4 1-.4 1.4 0z"/></svg>
          <span>(03) 9417 2608</span>
        </li>
        <li class="contact-item">
          <svg viewBox="0 0 16 16" aria-hidden="true"><path d="M1 3h14v10H1V3zm1.2 1.2v.3L8 8.6l5.8-4.1v-.3H2.2z"/></svg>
          <span>info@corvantela.com.au</span>
        </li>
        <li class="contact-item">
          <svg viewBox="0 0 16 16" aria-hidden="true"><path d="M8 0a8 8 0 1 0 0 16A8 8 0 0 0 8 0zm5.9 7.3h-2.6a12 12 0 0 0-1-4.9 6.5 6.5 0 0 1 3.6 4.9zM8 1.5c.9 1.1 1.6 3.2 1.8 5.8H6.2C6.4 4.7 7.1 2.6 8 1.5zM5.7 2.4a12 12 0 0 0-1 4.9H2.1a6.5 6.5 0 0 1 3.6-4.9zM2.1 8.7h2.6a12 12 0 0 0 1 4.9 6.5 6.5 0 0 1-3.6-4.9zM8 14.5c-.9-1.1-1.6-3.2-1.8-5.8h3.6c-.2 2.6-.9 4.7-1.8 5.8zm2.3-.9a12 12 0 0 0 1-4.9h2.6a6.5 6.5 0 0 1-3.6 4.9z"/></svg>
          <span>www.corvantela.com.au</span>
        </li>
      </ul>
    </div>
  </section>

</body>
</html>
```